promotional flyer for Valtera Gym

we are after a double sided a5 leaflet to promote our gym, this is to go out to the general public to entice them into getting membership.

gym membership is £30 per month

it should also include the offer of - if you present this leaflet then there will be no joining fee

some of the features of the gym include

strength machines
cardio machines
functional area
sprung floor mat area

Target Market(s)

Adults 16+ who want to go to the gym and workout

Industry/Entity Type

Gym

Font styles to use
Other font styles liked:
• montserrat Regular

Requirements
Must have
• Clean on brand design
• use images supplied by us
Nice to have
• focus on an inclusive experience as the gym will be advertised to everyone
• should also use our "fitter, stronger, Healthier"

```html
<!DOCTYPE html>
<html lang="en">
<head>
<meta charset="utf-8">
<title>Valtera Gym – A5 Leaflet</title>
<link href="https://fonts.googleapis.com/css2?family=Montserrat:wght@400;500;600;700;800&display=swap" rel="stylesheet">
<style>
  :root{
    --orange:#f15a29;
    --slate:#3e4750;
    --slate-dark:#2f363d;
    --white:#ffffff;
    --ink:#4a4f55;
    --bg:#e4e2de;
  }
  *{margin:0;padding:0;box-sizing:border-box}
  html,body{width:1200px;height:833px;overflow:hidden}
  body{background:var(--bg);font-family:'Montserrat',sans-serif;position:relative}
  .flyer{
    position:absolute;top:94px;width:583px;height:827px;
    transform:scale(0.7805);transform-origin:0 0;
    overflow:hidden;box-shadow:0 6px 18px rgba(0,0,0,.25);
    color:var(--white);
  }
  .flyer--front{left:117px}
  .flyer--back{left:627px}
  .flyer__art{position:absolute;inset:0;width:583px;height:827px}
  .abs{position:absolute}

  .brand-name{
    position:absolute;left:0;width:583px;text-align:center;
    font-weight:500;letter-spacing:4px;color:var(--white);text-transform:uppercase;
  }
  .tagline{
    position:absolute;left:0;width:583px;text-align:center;
    color:var(--orange);font-weight:600;letter-spacing:2.5px;
  }
  .badge{
    position:absolute;text-align:center;font-weight:700;line-height:1.15;color:var(--white);
  }

  /* front */
  .features__title{
    left:293px;top:455px;width:234px;height:32px;background:var(--orange);
    font-weight:700;font-size:17px;line-height:32px;padding-left:12px;
  }
  .features__list{left:295px;top:499px;list-style:none}
  .features__item{display:flex;align-items:center;height:30.5px;font-size:17px;font-weight:500;letter-spacing:.3px}
  .features__icon{width:23px;height:23px;background:var(--orange);border-radius:3px;margin-right:10px;display:flex;align-items:center;justify-content:center}
  .offer{
    left:308px;top:632px;width:275px;height:90px;background:var(--white);padding:5px;
  }
  .offer__inner{border:1.5px dashed #9aa0a6;border-right:none;height:100%;text-align:center;padding-top:8px}
  .offer__eyebrow{color:var(--ink);font-size:12.5px;font-weight:500}
  .offer__price{color:var(--orange);font-size:26px;font-weight:700;line-height:1.15;letter-spacing:.5px}
  .offer__note{color:var(--ink);font-size:8.5px;letter-spacing:-.1px;margin-top:3px}

  .contact{position:absolute;right:12px;bottom:14px;text-align:right;font-size:11px;font-weight:500;line-height:1.3}
  .contact__row{display:flex;justify-content:flex-end;align-items:center;gap:8px}
  .contact__row + .contact__row{margin-top:6px}
  .contact__icon{width:13px;height:13px;background:var(--white);border-radius:2px;flex:none;display:flex;align-items:center;justify-content:center}

  /* back */
  .headline{left:18px;top:36px;font-size:40px;font-weight:800;line-height:1.05;letter-spacing:0;white-space:nowrap}
  .intro{left:18px;top:143px;font-size:17px;line-height:22px;font-weight:400;white-space:nowrap}
  .intro p + p{margin-top:24px}
  .benefits__title{
    left:176px;top:533px;width:230px;height:28px;border-radius:14px;background:var(--orange);
    text-align:center;font-weight:700;font-size:16px;line-height:28px;letter-spacing:.5px;
  }
  .benefits__list{left:18px;top:590px;width:560px;list-style:none;display:grid;grid-template-columns:282px 270px;row-gap:14px}
  .benefits__item{display:flex;align-items:center;gap:8px;font-size:13px;font-weight:500;height:22px}
  .hours{left:20px;top:755px;font-size:13px;line-height:18px}
</style>
</head>
<body>

<!-- FRONT -->
<section class="flyer flyer--front">
  <svg class="flyer__art" viewBox="0 0 583 827">
    <defs>
      <radialGradient id="slateFront" cx="50%" cy="55%" r="70%">
        <stop offset="0" stop-color="#4a535c"/><stop offset="1" stop-color="#353c43"/>
      </radialGradient>
      <linearGradient id="photoCycle" x1="0" y1="0" x2="1" y2="1">
        <stop offset="0" stop-color="#4b5560"/><stop offset=".55" stop-color="#2b2f35"/><stop offset="1" stop-color="#7a2a35"/>
      </linearGradient>
      <linearGradient id="photoWeights" x1="0" y1="0" x2="1" y2="1">
        <stop offset="0" stop-color="#7b3a2e"/><stop offset=".5" stop-color="#3a3534"/><stop offset="1" stop-color="#5b5a5c"/>
      </linearGradient>
    </defs>
    <rect width="583" height="827" fill="url(#slateFront)"/>
    <g role="img" aria-label="Photo of two members riding exercise bikes in the cardio studio">
      <polygon points="0,0 583,0 583,226 0,303" fill="url(#photoCycle)"/>
    </g>
    <line x1="0" y1="304" x2="583" y2="227" stroke="var(--orange)" stroke-width="5"/>
    <rect x="0" y="722" width="583" height="105" fill="var(--orange)"/>
    <circle cx="-5" cy="822" r="336" fill="var(--white)"/>
    <circle cx="-5" cy="822" r="328" fill="var(--orange)"/>
    <g role="img" aria-label="Photo of a member training with dumbbells in the weights area">
      <circle cx="-5" cy="822" r="319" fill="url(#photoWeights)"/>
    </g>
    <circle cx="87" cy="517" r="77" fill="var(--white)"/>
    <circle cx="87" cy="517" r="73" fill="var(--orange)"/>
    <circle cx="87" cy="517" r="66" fill="var(--slate)" stroke="var(--white)" stroke-width="3"/>
    <circle cx="296" cy="264" r="60" fill="var(--slate)" stroke="var(--white)" stroke-width="7"/>
  </svg>

  <h1 class="brand-name" style="top:338px;font-size:46px">Valtera Gym</h1>
  <p class="tagline" style="top:398px;font-size:17px">FITTER &nbsp;|&nbsp; STRONGER &nbsp;|&nbsp; HEALTHIER</p>

  <p class="badge" style="left:19px;top:497px;width:136px;font-size:17px">GET STARTED<br>TODAY!</p>

  <h2 class="abs features__title">FEATURES OF THE GYM</h2>
  <ul class="abs features__list">
    <li class="features__item"><span class="features__icon"><svg width="15" height="15" viewBox="0 0 15 15"><rect x="1" y="3" width="3" height="9" fill="#fff"/><rect x="11" y="3" width="3" height="9" fill="#fff"/><rect x="4" y="6.3" width="7" height="2.4" fill="#fff"/></svg></span>STRENGTH MACHINES</li>
    <li class="features__item"><span class="features__icon"><svg width="15" height="15" viewBox="0 0 15 15"><path d="M7.5 13 L1.8 7.2 A3.2 3.2 0 0 1 7.5 3.4 A3.2 3.2 0 0 1 13.2 7.2 Z" fill="#fff"/></svg></span>CARDIO MACHINES</li>
    <li class="features__item"><span class="features__icon"><svg width="15" height="15" viewBox="0 0 15 15"><rect x="2" y="8" width="3" height="5" fill="#fff"/><rect x="6" y="5" width="3" height="8" fill="#fff"/><rect x="10" y="2" width="3" height="11" fill="#fff"/></svg></span>FUNCTIONAL AREA</li>
    <li class="features__item"><span class="features__icon"><svg width="15" height="15" viewBox="0 0 15 15"><rect x="4" y="1.5" width="7" height="4" rx="2" fill="none" stroke="#fff" stroke-width="1.6"/><circle cx="7.5" cy="9" r="4.5" fill="#fff"/></svg></span>SPRUNG FLOOR MAT AREA</li>
  </ul>

  <div class="abs offer">
    <div class="offer__inner">
      <p class="offer__eyebrow">BECOME A MEMBER</p>
      <p class="offer__price">£30 PER MONTH</p>
      <p class="offer__note">If you present this leaflet then there will be no joining fee</p>
    </div>
  </div>

  <address class="contact" style="font-style:normal">
    <div class="contact__row">01632 960418<span class="contact__icon"><svg width="9" height="9" viewBox="0 0 9 9"><path d="M2 1 L3.5 1 L4 3 L3 3.8 Q4 5.8 5.2 6 L6 5 L8 5.5 L8 7 Q4 8 1.5 3 Z" fill="var(--orange)"/></svg></span></div>
    <div class="contact__row">www.valteragym.co.uk<span class="contact__icon"><svg width="9" height="9" viewBox="0 0 9 9"><circle cx="4.5" cy="4.5" r="3.4" fill="none" stroke="var(--orange)" stroke-width="1.2"/></svg></span></div>
    <div class="contact__row"><span>Unit 4 Harbour Row, Elm Crescent,<br>Westbrook, West Sussex, BN00 1AA</span><span class="contact__icon"><svg width="9" height="9" viewBox="0 0 9 9"><path d="M4.5 8.5 L2 4.5 A2.6 2.6 0 1 1 7 4.5 Z" fill="var(--orange)"/></svg></span></div>
  </address>
</section>

<!-- BACK -->
<section class="flyer flyer--back">
  <svg class="flyer__art" viewBox="0 0 583 827">
    <defs>
      <radialGradient id="slateBack" cx="50%" cy="60%" r="70%">
        <stop offset="0" stop-color="#4a535c"/><stop offset="1" stop-color="#353c43"/>
      </radialGradient>
      <linearGradient id="photoPress" x1="0" y1="0" x2="1" y2="1">
        <stop offset="0" stop-color="#5a2a36"/><stop offset=".45" stop-color="#3b3a3d"/><stop offset="1" stop-color="#7d7f84"/>
      </linearGradient>
    </defs>
    <rect width="583" height="827" fill="url(#slateBack)"/>
    <polygon points="0,0 583,0 583,300 0,385" fill="var(--orange)"/>
    <line x1="0" y1="388" x2="583" y2="303" stroke="var(--white)" stroke-width="5"/>
    <circle cx="472" cy="125" r="207" fill="var(--slate)"/>
    <circle cx="472" cy="125" r="199" fill="var(--white)"/>
    <g role="img" aria-label="Photo of a member doing a seated dumbbell shoulder press">
      <circle cx="472" cy="125" r="191" fill="url(#photoPress)"/>
    </g>
    <circle cx="465" cy="323" r="77" fill="var(--white)"/>
    <circle cx="465" cy="323" r="73" fill="var(--orange)"/>
    <circle cx="465" cy="323" r="66" fill="var(--slate)" stroke="var(--white)" stroke-width="3"/>
    <circle cx="297" cy="363" r="50" fill="var(--slate)" stroke="var(--white)" stroke-width="6"/>
    <rect x="0" y="727" width="583" height="4" fill="var(--white)"/>
    <rect x="0" y="731" width="583" height="96" fill="var(--orange)"/>
  </svg>

  <h2 class="abs headline">BECOME A<br>MEMBER</h2>
  <div class="abs intro">
    <p>Membership fee is<br><strong>£30/month</strong> with a £30<br>joining fee and no contract!</p>
    <p>If you present this leaflet then<br>there will be no joining fee!</p>
  </div>

  <p class="badge" style="left:397px;top:304px;width:136px;font-size:17px">GET STARTED<br>TODAY!</p>

  <h1 class="brand-name" style="top:428px;font-size:42px">Valtera Gym</h1>
  <p class="tagline" style="top:476px;font-size:15px">FITTER &nbsp;|&nbsp; STRONGER &nbsp;|&nbsp; HEALTHIER</p>

  <h2 class="abs benefits__title">BENEFITS</h2>
  <ul class="abs benefits__list">
    <li class="benefits__item"><svg width="16" height="16" viewBox="0 0 16 16"><circle cx="8" cy="8" r="6.5" fill="none" stroke="#fff" stroke-width="1.3"/><path d="M5 8 L7.3 10.3 L11.5 5.5" fill="none" stroke="var(--orange)" stroke-width="1.8"/></svg>WIDE VARIETY OF MACHINES</li>
    <li class="benefits__item"><svg width="16" height="16" viewBox="0 0 16 16"><circle cx="8" cy="8" r="6.5" fill="none" stroke="#fff" stroke-width="1.3"/><path d="M5 8 L7.3 10.3 L11.5 5.5" fill="none" stroke="var(--orange)" stroke-width="1.8"/></svg>FUNCTIONAL MAT AREA</li>
    <li class="benefits__item"><svg width="16" height="16" viewBox="0 0 16 16"><circle cx="8" cy="8" r="6.5" fill="none" stroke="#fff" stroke-width="1.3"/><path d="M5 8 L7.3 10.3 L11.5 5.5" fill="none" stroke="var(--orange)" stroke-width="1.8"/></svg>GREAT ATMOSPHERE</li>
    <li class="benefits__item"><svg width="16" height="16" viewBox="0 0 16 16"><circle cx="8" cy="8" r="6.5" fill="none" stroke="#fff" stroke-width="1.3"/><path d="M5 8 L7.3 10.3 L11.5 5.5" fill="none" stroke="var(--orange)" stroke-width="1.8"/></svg>PERSONAL TRAINERS AVAILABLE</li>
    <li class="benefits__item"><svg width="16" height="16" viewBox="0 0 16 16"><circle cx="8" cy="8" r="6.5" fill="none" stroke="#fff" stroke-width="1.3"/><path d="M5 8 L7.3 10.3 L11.5 5.5" fill="none" stroke="var(--orange)" stroke-width="1.8"/></svg>FRIENDLY &amp; KNOWLEDGEABLE TEAM</li>
    <li class="benefits__item"><svg width="16" height="16" viewBox="0 0 16 16"><circle cx="8" cy="8" r="6.5" fill="none" stroke="#fff" stroke-width="1.3"/><path d="M5 8 L7.3 10.3 L11.5 5.5" fill="none" stroke="var(--orange)" stroke-width="1.8"/></svg>FULL CHANGING FACILITIES</li>
  </ul>

  <p class="abs hours">OPENING HOURS:<br>Monday to Friday 6am to 10PM,<br>Saturday and Sunday 7am to 7pm</p>

  <address class="contact" style="font-style:normal">
    <div class="contact__row">01632 960418<span class="contact__icon"><svg width="9" height="9" viewBox="0 0 9 9"><path d="M2 1 L3.5 1 L4 3 L3 3.8 Q4 5.8 5.2 6 L6 5 L8 5.5 L8 7 Q4 8 1.5 3 Z" fill="var(--orange)"/></svg></span></div>
    <div class="contact__row">www.valteragym.co.uk<span class="contact__icon"><svg width="9" height="9" viewBox="0 0 9 9"><circle cx="4.5" cy="4.5" r="3.4" fill="none" stroke="var(--orange)" stroke-width="1.2"/></svg></span></div>
    <div class="contact__row"><span>Unit 4 Harbour Row, Elm Crescent,<br>Westbrook, West Sussex, BN00 1AA</span><span class="contact__icon"><svg width="9" height="9" viewBox="0 0 9 9"><path d="M4.5 8.5 L2 4.5 A2.6 2.6 0 1 1 7 4.5 Z" fill="var(--orange)"/></svg></span></div>
  </address>
</section>

</body>
</html>
```